Engineering group involved with fire safety needs a business card

We need a business card design for a company based in Greece called "Varotis Group". We are engineers and specialized technicians, operating the following : a) Fire fighting equipment trade b) Installation , Inspection & Maintenance of fire extinguishers and fire protection systems c) Occupational Health & Safety (Risk assessment & management/ Staff training). We need a clear and simple card design. I uploaded a draft I made, in order to give you an idea of the company and how I currently imagine the design of the card. I also uploaded the logo in .png file format. We are always open to different, new suggestions and ideas you may want to submit.
Target Market(s)
industries, companies, managers, retail clients
Industry/Entity Type
Fire Safety
Contact Information for Business Card
Addresses & phone numbers (headquarters + branch), logo, name (you can find all the details on the uploaded files!)
Colors
Designer to choose colors to be used in the design.
Look and feel
Each slider illustrates characteristics of the customer's brand and the style your logo design should communicate.

```html
<!DOCTYPE html>
<html lang="en">
<head>
<meta charset="utf-8">
<title>Varotis Group – Business Card</title>
<link rel="stylesheet" href="https://fonts.googleapis.com/css2?family=Montserrat:wght@300;400;500;700;800&family=Oswald:wght@500&display=swap">
<style>
  :root {
    --red: #b3202a;
    --charcoal: #3b3e42;
    --charcoal-deep: #2f3235;
    --stage: #24262a;
    --ink: #4a4a4a;
    --muted: #6b6b6b;
    --rule: #9a9a9a;
    --white: #ffffff;
  }
  * { box-sizing: border-box; margin: 0; padding: 0; }
  html, body { width: 1200px; height: 900px; overflow: hidden; }
  body {
    background: var(--stage);
    font-family: "Montserrat", sans-serif;
    position: relative;
  }
  .card {
    position: absolute;
    top: 152px;
    width: 340px;
    height: 595px;
    overflow: hidden;
    box-shadow: 0 18px 40px rgba(0,0,0,.45);
  }
  /* Front */
  .card-front { left: 200px; background: var(--white); }
  .front-header {
    height: 172px;
    background: var(--red);
    display: flex;
    flex-direction: column;
    justify-content: center;
    align-items: center;
    border-bottom: 4px solid var(--white);
    box-shadow: 0 3px 0 var(--red);
  }
  .wordmark {
    color: var(--white);
    font-weight: 700;
    text-transform: uppercase;
    text-align: center;
    line-height: 1;
  }
  .front-header .wordmark-main { font-size: 50px; letter-spacing: 1px; }
  .front-header .wordmark-sub { font-size: 26px; letter-spacing: 5px; margin-top: 6px; }

  .person { padding: 150px 36px 0 36px; }
  .person-name {
    color: var(--red);
    font-weight: 800;
    font-size: 21px;
    letter-spacing: .5px;
    text-transform: uppercase;
  }
  .person-role { color: var(--muted); font-size: 13px; margin-top: 2px; }
  .person-rule { border: 0; border-top: 1px solid var(--rule); margin: 10px 0 12px; }

  .contact-list { list-style: none; }
  .contact-list li {
    display: flex;
    align-items: center;
    gap: 10px;
    font-size: 12.5px;
    color: var(--ink);
    line-height: 1.55;
  }
  .contact-list svg { width: 14px; height: 14px; flex: none; }
  .addresses { margin-top: 16px; font-size: 13px; color: var(--ink); line-height: 1.5; }
  .addresses b { color: var(--red); font-weight: 700; }

  /* Back */
  .card-back {
    left: 660px;
    background: linear-gradient(160deg, var(--charcoal) 0%, var(--charcoal-deep) 100%);
    color: var(--white);
    text-align: center;
  }
  .back-brand { padding-top: 96px; display: flex; flex-direction: column; align-items: center; }
  .brand-square { width: 34px; height: 34px; background: var(--white); margin-bottom: 16px; }
  .card-back .wordmark-main { font-size: 44px; letter-spacing: 1px; }
  .card-back .wordmark-sub { font-size: 22px; letter-spacing: 5px; margin-top: 5px; }
  .service-band {
    margin-top: 36px;
    background: var(--red);
    font-family: "Oswald", sans-serif;
    font-weight: 500;
    font-size: 16px;
    letter-spacing: .5px;
    padding: 7px 0;
  }
  .services {
    list-style: none;
    margin-top: 22px;
    font-weight: 300;
    font-size: 13.5px;
    letter-spacing: .6px;
    line-height: 1.45;
    text-transform: uppercase;
  }
  .back-contact { margin-top: 22px; font-size: 14px; line-height: 1.5; font-weight: 400; }
</style>
</head>
<body>

<section class="card card-front" aria-label="Business card front">
  <header class="front-header">
    <div class="wordmark wordmark-main">Varotis</div>
    <div class="wordmark wordmark-sub">Group</div>
  </header>

  <div class="person">
    <h1 class="person-name">Nikolas Andreou</h1>
    <p class="person-role">Mechanical Engineer | OHS Consultant</p>
    <hr class="person-rule">

    <ul class="contact-list">
      <li>
        <svg viewBox="0 0 16 16" aria-hidden="true"><circle cx="8" cy="8" r="7" fill="none" stroke="var(--red)" stroke-width="1.4"/><path d="M5.5 5l1.3-.4.8 1.7-.8.6c.4.9 1 1.5 1.9 1.9l.6-.8 1.7.8-.4 1.3c-2.8 0-5.1-2.3-5.1-5.1z" fill="var(--red)"/></svg>
        (HQ) +30 22920 41380
      </li>
      <li>
        <svg viewBox="0 0 16 16" aria-hidden="true"><circle cx="8" cy="8" r="7" fill="none" stroke="var(--red)" stroke-width="1.4"/><path d="M5.5 5l1.3-.4.8 1.7-.8.6c.4.9 1 1.5 1.9 1.9l.6-.8 1.7.8-.4 1.3c-2.8 0-5.1-2.3-5.1-5.1z" fill="var(--red)"/></svg>
        (BO) +30 210 6124957
      </li>
      <li>
        <svg viewBox="0 0 16 16" aria-hidden="true"><rect x="4" y="1.5" width="8" height="13" rx="1.5" fill="none" stroke="var(--red)" stroke-width="1.4"/><circle cx="8" cy="12" r=".9" fill="var(--red)"/></svg>
        +30 694 215 73 08
      </li>
      <li>
        <svg viewBox="0 0 16 16" aria-hidden="true"><rect x="1.5" y="3.5" width="13" height="9" fill="none" stroke="var(--red)" stroke-width="1.4"/><path d="M1.5 3.5L8 9l6.5-5.5" fill="none" stroke="var(--red)" stroke-width="1.4"/></svg>
        n.andreou@varotisgroup.gr
      </li>
      <li>
        <svg viewBox="0 0 16 16" aria-hidden="true"><circle cx="8" cy="8" r="6.5" fill="none" stroke="var(--red)" stroke-width="1.4"/><ellipse cx="8" cy="8" rx="2.8" ry="6.5" fill="none" stroke="var(--red)" stroke-width="1.2"/><path d="M1.5 8h13" stroke="var(--red)" stroke-width="1.2"/></svg>
        www.varotisgroup.gr
      </li>
    </ul>

    <p class="addresses">
      <b>HQ:</b> 12 Elaion Street, 18531 Piraeus<br>
      <b>BO:</b> 45 Kifisias Lane, 14562 Kifisia
    </p>
  </div>
</section>

<section class="card card-back" aria-label="Business card back">
  <div class="back-brand">
    <span class="brand-square" aria-hidden="true"></span>
    <div class="wordmark wordmark-main">Varotis</div>
    <div class="wordmark wordmark-sub">Group</div>
  </div>

  <p class="service-band">Installation – Inspection – Maintenance</p>

  <ul class="services">
    <li>Fire Fighting Equipment</li>
    <li>Licensing &amp; Business Registration</li>
    <li>Occupational Health &amp; Safety</li>
    <li>Staff Training</li>
  </ul>

  <p class="back-contact">
    info@varotisgroup.gr<br>
    www.varotisgroup.gr
  </p>
</section>

</body>
</html>
```